Marrowind Labs - pioneers of next generation consulting!

We are a next generation management consulting firm with two focus areas and USPs (unique selling points):>Technology driven business developmentWe are not developers, we are experts in HOW to apply and incorporate technology in your business dna to drive business growth and value-added change.>Creating high performing teams levering our philosophy of collective intelligence. We truly understand the need of human engagement and we know that the only way of getting there is by building strong relationships among people, a warm and open culture is a stepping stone towards effective collaboration within/among teams. - We don't want a ”corporate feel” to our templates. The organic feeling we have with our blue-on-blue blobs has the idea of ever changing movement and shape changing. Please see our website, www.marrowindlabs.se. - In our context we sit among classic business mgmt. consultants and classic IT mgmt. consultants. We cater to business, tech and humans as the ultimate vehicle of change and business value. -To have a clean template one suggestion is to only use blue, white and black and keeping other colors separate, as an alternative but we are truly open allow your creativity add value to this. We are looking to find a slide deck which we can pick slides from, depending on what/whom/why we interact with customer we want to create different outcomes and our presentations should support this.

Industry/Entity Type

Management Consulting

Requirements
Must have
• next generation powerpoint and how to package storytelling. please keep to our look and feel, we just arrived at our logo, colours and shapes. Help us to carry it into our ppt's as well.
Should not have
• Hi all, please have a look at our website. It is still very new and more will be done, but our goal is to make powerpoint to come alive again and mirror our pioneering hearts and brains.

```html
<!DOCTYPE html>
<html lang="en">
<head>
<meta charset="utf-8">
<title>Marrowind Labs – Deck Overview</title>
<link href="https://fonts.googleapis.com/css2?family=Permanent+Marker&family=Nanum+Gothic+Coding:wght@400;700&family=Roboto+Condensed:wght@300;400;700&display=swap" rel="stylesheet">
<style>
:root{
  --navy:#1d3f87;
  --deep:#183774;
  --blue:#2a5db0;
  --sky:#2e6ac4;
  --pale:#dfe6f3;
  --ink:#1e2233;
  --grey:#8a90a0;
  --line:#d8dce6;
  --white:#ffffff;
}
*{margin:0;padding:0;box-sizing:border-box}
html,body{width:1200px;height:512px;overflow:hidden;background:var(--white)}
body{position:relative;font-family:"Nanum Gothic Coding",monospace;color:var(--ink)}
.icon-library{position:absolute;width:0;height:0;overflow:hidden}
.slide{position:absolute;width:284px;height:164px;overflow:hidden;background:var(--white)}
.slide--navy{background:var(--navy)}
.slide--sky{background:var(--sky)}
.c1{left:12px}.c2{left:302px}.c3{left:598px}.c4{left:894px}
.r1{top:2px}.r2{top:170px}.r3{top:338px}

.footer{position:absolute;left:0;bottom:0;width:100%;height:14px}
.footer svg{position:absolute;left:0;bottom:0;width:100%;height:9px}
.brand{position:absolute;right:8px;bottom:6px;font-family:"Roboto Condensed",sans-serif;font-weight:700;font-size:7px;letter-spacing:.4px;color:var(--ink);text-transform:uppercase}
.slide--navy .brand,.slide--sky .brand{color:var(--white)}
.pager{position:absolute;left:6px;bottom:10px;width:6px;height:2px;background:var(--navy)}
.slide--navy .pager,.slide--sky .pager{background:var(--white)}

.kicker{position:absolute;width:100%;text-align:center;font-size:3.5px;letter-spacing:1px;color:var(--ink);text-transform:uppercase}
.heading{position:absolute;width:100%;text-align:center;font-family:"Permanent Marker",cursive;font-weight:400;font-size:11px;color:var(--navy);letter-spacing:.5px;text-transform:uppercase}
.tiny{font-size:3.2px;line-height:1.5;color:var(--ink)}

/* statistic chart */
.stat-lead{position:absolute;left:12px;top:54px;width:80px}
.stat-lead b{font-size:4.6px;font-weight:700}
.stat-note{position:absolute;left:12px;top:118px;width:80px;color:var(--navy)}
.stat-row{position:absolute;left:104px;width:170px;height:38px}
.stat-badge{position:absolute;left:0;top:0;width:34px;height:34px;border-radius:50%;background:var(--pale);display:flex;align-items:center;justify-content:center}
.stat-badge span{width:26px;height:26px;border-radius:50%;background:var(--navy);color:var(--white);font-weight:700;font-size:6px;display:flex;align-items:center;justify-content:center}
.bar{position:absolute;height:4px;background:linear-gradient(90deg,var(--deep),var(--blue));border-radius:0 2px 2px 0}
.bar em{position:absolute;right:2px;top:0;font-style:normal;font-size:2.6px;line-height:4px;color:var(--white)}
.axis{position:absolute;left:40px;width:130px;display:flex;justify-content:space-between;font-size:2.4px;color:var(--grey)}

/* matrix */
.matrix{position:absolute;left:48px;top:49px;display:grid;grid-template-columns:repeat(3,62px);gap:4px 6px}
.cell{height:21px;background:var(--white);box-shadow:0 0 2px rgba(0,0,0,.18);display:flex;flex-direction:column;align-items:center;justify-content:center;gap:2px;font-size:3px;color:var(--grey)}
.cell i{width:4px;height:3px;background:var(--navy);border-radius:.5px}
.cell--on{background:var(--navy);color:var(--white)}
.cell--on i{background:var(--white)}
.matrix-axis{position:absolute;left:42px;top:46px;width:1px;height:82px;background:var(--line)}
.matrix-base{position:absolute;left:42px;top:128px;width:198px;height:1px;background:var(--line)}
.axis-label{position:absolute;font-size:2.6px;color:var(--grey)}

/* service */
.svc-intro{position:absolute;left:40px;top:38px;width:204px;text-align:center}
.svc-band{position:absolute;left:0;top:66px;width:100%;height:78px;background:linear-gradient(120deg,#1b3366,#2c4f8f 55%,#1c3570)}
.svc-cols{position:absolute;left:8px;top:82px;width:268px;display:grid;grid-template-columns:repeat(4,1fr)}
.svc{padding:0 5px;border-left:1px solid rgba(255,255,255,.6);color:var(--white)}
.svc:first-child{border-left:none}
.svc svg{display:block;width:8px;height:8px;margin:0 auto;color:var(--white)}
.svc b{display:block;font-size:4.2px;font-weight:400;margin:6px 0 3px}
.svc p{font-size:2.8px;line-height:1.5;opacity:.85}

/* chart diagram */
.chart-photo{position:absolute;left:0;top:0;width:100%;height:152px;background:linear-gradient(140deg,#2a4a8c,#1d3c80 45%,#183774)}
.chart-white{position:absolute;left:0;top:0;width:100%;height:164px}
.chart-card{position:absolute;left:102px;top:30px;width:174px;height:114px;background:var(--white);box-shadow:0 0 4px rgba(0,0,0,.2)}
.chart-title{position:absolute;left:24px;top:86px;font-family:"Permanent Marker",cursive;font-weight:400;font-size:12px;line-height:1.1;color:var(--navy);text-transform:uppercase}
.chart-kick{position:absolute;left:24px;top:80px;font-size:3px;letter-spacing:.6px;text-transform:uppercase}
.donuts{position:absolute;left:8px;top:86px;display:flex;gap:20px}
.donut{display:flex;flex-direction:column;align-items:center;gap:3px;font-size:2.6px}
.donut svg{width:18px;height:18px}
.chart-note{position:absolute;left:118px;top:94px;width:50px}

/* contact */
.contact-title{position:absolute;left:12px;top:30px;font-family:"Roboto Condensed",sans-serif;font-weight:400;font-size:9.5px;line-height:1.25;letter-spacing:1px;color:var(--navy)}
.contact-title strong{font-family:"Permanent Marker",cursive;font-weight:400;letter-spacing:.5px}
.contact-lead{position:absolute;left:12px;top:74px;width:88px}
.contact-list{position:absolute;left:12px;top:104px;list-style:none}
.contact-list li{display:flex;align-items:center;gap:5px;font-size:2.9px;margin-bottom:4.5px}
.contact-list svg{width:4px;height:4px;color:var(--ink)}
.divider{position:absolute;left:124px;top:0;height:150px;border-left:1px dashed var(--ink)}
.map{position:absolute;left:150px;top:18px;width:118px;height:100px;background:linear-gradient(135deg,#2b2f38,#1f2d4a 55%,#2a3f78);box-shadow:2px 4px 8px rgba(0,0,0,.4)}

/* icon sheets */
.icons{position:absolute;display:grid;justify-items:center;align-items:center}
.icons svg{display:block}
.icons--dense{left:24px;top:24px;width:236px;grid-template-columns:repeat(16,1fr);row-gap:6px;color:var(--white)}
.icons--dense svg{width:5px;height:5px}
.icons--large{left:16px;top:34px;width:252px;grid-template-columns:repeat(12,1fr);row-gap:9px;color:var(--navy)}
.icons--large svg{width:12px;height:12px}
.icons--ink{left:16px;top:22px;width:252px;grid-template-columns:repeat(14,1fr);row-gap:11px;color:var(--ink)}
.icons--ink svg{width:7px;height:7px}
.icons--sky{left:20px;top:18px;width:244px;grid-template-columns:repeat(16,1fr);row-gap:7px;color:var(--white)}
.icons--sky svg{width:6px;height:6px}

/* feature copy */
.features{position:absolute;left:600px;top:338px;width:584px;height:150px;display:flex;flex-direction:column;justify-content:center;align-items:center;gap:17px;font-family:"Roboto Condensed",sans-serif;font-weight:400;font-size:15px;letter-spacing:.3px;color:var(--ink);text-transform:uppercase}
</style>
</head>
<body>

<svg class="icon-library" aria-hidden="true">
  <symbol id="home" viewBox="0 0 24 24" fill="currentColor"><path d="M12 3 2 12h3v9h5v-6h4v6h5v-9h3z"/></symbol>
  <symbol id="bank" viewBox="0 0 24 24" fill="currentColor"><path d="M12 2 2 7v2h20V7zM4 10h3v8H4zm6.5 0h3v8h-3zM17 10h3v8h-3zM2 19h20v3H2z"/></symbol>
  <symbol id="calendar" viewBox="0 0 24 24" fill="currentColor"><path fill-rule="evenodd" d="M3 5h18v16H3zM5 10v9h14v-9z"/><path d="M7 2h2v3H7zm8 0h2v3h-2zM7 12h3v3H7z"/></symbol>
  <symbol id="bars" viewBox="0 0 24 24" fill="currentColor"><path d="M3 20h18v2H3zM5 12h3v7H5zm5-6h3v13h-3zm5 3h3v10h-3z"/></symbol>
  <symbol id="linechart" viewBox="0 0 24 24" fill="currentColor"><path d="M3 3h2v16h16v2H3z"/><path d="m6 15 4-5 3 3 6-7" fill="none" stroke="currentColor" stroke-width="2.2"/></symbol>
  <symbol id="pie" viewBox="0 0 24 24" fill="currentColor"><path d="M11 3a9 9 0 1 0 9 10h-9z"/><path d="M13 1v10h10A10 10 0 0 0 13 1z"/></symbol>
  <symbol id="search" viewBox="0 0 24 24"><circle cx="10" cy="10" r="6" fill="none" stroke="currentColor" stroke-width="3"/><path d="m14 14 7 7" stroke="currentColor" stroke-width="3.5"/></symbol>
  <symbol id="gear" viewBox="0 0 24 24"><circle cx="12" cy="12" r="8.5" fill="none" stroke="currentColor" stroke-width="3.5" stroke-dasharray="3.3 3.4"/><circle cx="12" cy="12" r="5.5" fill="none" stroke="currentColor" stroke-width="3.5"/></symbol>
  <symbol id="bulb" viewBox="0 0 24 24" fill="currentColor"><circle cx="12" cy="9" r="7"/><path d="M9 15h6v4H9zm1 5h4v2h-4z"/></symbol>
  <symbol id="lock" viewBox="0 0 24 24" fill="currentColor"><path d="M5 11h14v11H5z"/><path d="M8 11V7a4 4 0 0 1 8 0v4" fill="none" stroke="currentColor" stroke-width="2.5"/></symbol>
  <symbol id="mail" viewBox="0 0 24 24" fill="currentColor"><path fill-rule="evenodd" d="M2 5h20v14H2zm2 1.5 8 6 8-6z"/></symbol>
  <symbol id="phone" viewBox="0 0 24 24" fill="currentColor"><path d="M5 2h4l2 5-2.5 1.5a11 11 0 0 0 7 7L17 13l5 2v4a2 2 0 0 1-2 2A18 18 0 0 1 3 4a2 2 0 0 1 2-2z"/></symbol>
  <symbol id="pin" viewBox="0 0 24 24" fill="currentColor"><path fill-rule="evenodd" d="M12 1a8 8 0 0 1 8 8c0 6-8 14-8 14S4 15 4 9a8 8 0 0 1 8-8zm0 5a3 3 0 1 0 0 6 3 3 0 0 0 0-6z"/></symbol>
  <symbol id="user" viewBox="0 0 24 24" fill="currentColor"><circle cx="12" cy="7" r="5"/><path d="M3 22a9 8 0 0 1 18 0z"/></symbol>
  <symbol id="star" viewBox="0 0 24 24" fill="currentColor"><path d="m12 2 3 7 7 .6-5.4 4.7 1.7 7.2L12 17.7l-6.3 3.8 1.7-7.2L2 9.6 9 9z"/></symbol>
  <symbol id="heart" viewBox="0 0 24 24" fill="currentColor"><path d="M12 21 3 12a5 5 0 0 1 9-6 5 5 0 0 1 9 6z"/></symbol>
  <symbol id="check" viewBox="0 0 24 24"><path d="m3 12 6 6L21 6" fill="none" stroke="currentColor" stroke-width="3.5"/></symbol>
  <symbol id="close" viewBox="0 0 24 24"><path d="M4 4l16 16M20 4 4 20" fill="none" stroke="currentColor" stroke-width="3.5"/></symbol>
  <symbol id="plus" viewBox="0 0 24 24" fill="currentColor"><path d="M10 3h4v18h-4zM3 10h18v4H3z"/></symbol>
  <symbol id="arrow" viewBox="0 0 24 24" fill="currentColor"><path d="M2 10h13V5l7 7-7 7v-5H2z"/></symbol>
  <symbol id="clock" viewBox="0 0 24 24" fill="currentColor"><circle cx="12" cy="12" r="9" fill="none" stroke="currentColor" stroke-width="2.5"/><path d="M11 6h2v6h5v2h-7z"/></symbol>
  <symbol id="globe" viewBox="0 0 24 24" fill="none" stroke="currentColor" stroke-width="2"><circle cx="12" cy="12" r="9.5"/><ellipse cx="12" cy="12" rx="4" ry="9.5"/><path d="M2.5 12h19M4 7h16M4 17h16"/></symbol>
  <symbol id="folder" viewBox="0 0 24 24" fill="currentColor"><path d="M2 5h8l2 2h10v13H2z"/></symbol>
  <symbol id="doc" viewBox="0 0 24 24" fill="currentColor"><path fill-rule="evenodd" d="M5 2h10l5 5v15H5zm3 9v2h9v-2zm0 4v2h9v-2z"/></symbol>
  <symbol id="camera" viewBox="0 0 24 24" fill="currentColor"><path fill-rule="evenodd" d="M2 7h5l2-3h6l2 3h5v13H2zm10 3a4 4 0 1 0 0 8 4 4 0 0 0 0-8z"/></symbol>
  <symbol id="music" viewBox="0 0 24 24" fill="currentColor"><path d="M9 3h12v13.5a3 3 0 1 1-2-2.8V7h-8v11.5a3 3 0 1 1-2-2.8z"/></symbol>
  <symbol id="cloud" viewBox="0 0 24 24" fill="currentColor"><path d="M7 19a5 5 0 0 1-.5-10A6 6 0 0 1 18 8a5.5 5.5 0 0 1 0 11z"/></symbol>
  <symbol id="download" viewBox="0 0 24 24" fill="currentColor"><path d="M10 2h4v9h4l-6 7-6-7h4zM3 19h18v3H3z"/></symbol>
  <symbol id="wifi" viewBox="0 0 24 24" fill="currentColor"><path d="M2 9a14 14 0 0 1 20 0M5.5 12.5a9 9 0 0 1 13 0M9 16a4 4 0 0 1 6 0" fill="none" stroke="currentColor" stroke-width="2.5"/><circle cx="12" cy="19.5" r="2"/></symbol>
  <symbol id="battery" viewBox="0 0 24 24" fill="currentColor"><path d="M9 2h6v2h3v18H6V4h3z"/></symbol>
  <symbol id="bell" viewBox="0 0 24 24" fill="currentColor"><path d="M12 2a6 6 0 0 1 6 6v6l3 3v1H3v-1l3-3V8a6 6 0 0 1 6-6zm-3 17h6a3 3 0 0 1-6 0z"/></symbol>
  <symbol id="trash" viewBox="0 0 24 24" fill="currentColor"><path d="M4 5h16v2H4zm5-3h6v2H9zM6 8h12l-1 14H7z"/></symbol>
  <symbol id="plane" viewBox="0 0 24 24" fill="currentColor"><path d="M21 16v-2l-8-5V3.5a1.5 1.5 0 0 0-3 0V9l-8 5v2l8-2.5V19l-2 1.5V22l3.5-1 3.5 1v-1.5L13 19v-5.5z"/></symbol>
  <symbol id="rocket" viewBox="0 0 24 24" fill="currentColor"><path fill-rule="evenodd" d="M12 1c4 3 5 8 4 13l2 3v4l-3-2H9l-3 2v-4l2-3C7 9 8 4 12 1zm0 6a2 2 0 1 0 0 4 2 2 0 0 0 0-4z"/></symbol>
  <symbol id="target" viewBox="0 0 24 24" fill="currentColor"><circle cx="12" cy="12" r="9.5" fill="none" stroke="currentColor" stroke-width="2.2"/><circle cx="12" cy="12" r="5" fill="none" stroke="currentColor" stroke-width="2.2"/><circle cx="12" cy="12" r="1.8"/></symbol>
  <symbol id="flag" viewBox="0 0 24 24" fill="currentColor"><path d="M4 2h2v20H4zm3 1h13l-3 4 3 4H7z"/></symbol>
  <symbol id="trophy" viewBox="0 0 24 24" fill="currentColor"><path d="M6 2h12v6a6 6 0 0 1-12 0zM2 4h4v2H4a3 3 0 0 0 2 3v2a5 5 0 0 1-4-5zm20 0h-4v2h2a3 3 0 0 1-2 3v2a5 5 0 0 0 4-5zM11 14h2v4h-2zm-4 5h10v3H7z"/></symbol>
  <symbol id="briefcase" viewBox="0 0 24 24" fill="currentColor"><path d="M2 7h20v13H2zM9 3h6v4h-2V5h-2v2H9z"/></symbol>
  <symbol id="cart" viewBox="0 0 24 24" fill="currentColor"><path d="M1 3h4l3 11h11l3-8H7" fill="none" stroke="currentColor" stroke-width="2.2"/><circle cx="9" cy="19" r="2"/><circle cx="18" cy="19" r="2"/></symbol>
  <symbol id="tag" viewBox="0 0 24 24" fill="currentColor"><path fill-rule="evenodd" d="M2 2h10l10 10-10 10L2 12zm5 3a2 2 0 1 0 0 4 2 2 0 0 0 0-4z"/></symbol>
  <symbol id="key" viewBox="0 0 24 24" fill="currentColor"><circle cx="7" cy="12" r="5"/><path d="M11 10.5h11v3h-2v3h-3v-3h-6z"/></symbol>
  <symbol id="chat" viewBox="0 0 24 24" fill="currentColor"><path d="M2 3h20v14H9l-5 4v-4H2z"/></symbol>
  <symbol id="eye" viewBox="0 0 24 24" fill="currentColor"><path fill-rule="evenodd" d="M1 12C5 5 19 5 23 12c-4 7-18 7-22 0zm11-4a4 4 0 1 0 0 8 4 4 0 0 0 0-8z"/></symbol>
  <symbol id="cup" viewBox="0 0 24 24" fill="currentColor"><path d="M3 6h14v8a5 5 0 0 1-5 5H8a5 5 0 0 1-5-5zm14 2h2a3 3 0 0 1 0 6h-2v-2h2a1 1 0 0 0 0-2h-2zM2 20h16v2H2z"/></symbol>
  <symbol id="monitor" viewBox="0 0 24 24" fill="currentColor"><path fill-rule="evenodd" d="M2 3h20v14H2zm2 2v10h16V5z"/><path d="M10 17h4v3h3v2H7v-2h3z"/></symbol>
  <symbol id="calculator" viewBox="0 0 24 24" fill="currentColor"><path fill-rule="evenodd" d="M4 2h16v20H4zm2 2v4h12V4zm0 7v3h3v-3zm4.5 0v3h3v-3zM15 11v3h3v-3zm-9 5v3h3v-3zm4.5 0v3h3v-3zM15 16v3h3v-3z"/></symbol>
  <symbol id="shield" viewBox="0 0 24 24" fill="currentColor"><path d="M12 1 3 5v6c0 6 4 10 9 12 5-2 9-6 9-12V5z"/></symbol>
  <symbol id="drop" viewBox="0 0 24 24" fill="currentColor"><path d="M12 2s7 8 7 13a7 7 0 0 1-14 0c0-5 7-13 7-13z"/></symbol>
  <symbol id="flask" viewBox="0 0 24 24" fill="currentColor"><path d="M9 2h6v2h-1v5l6 11a1.5 1.5 0 0 1-1.3 2H5.3A1.5 1.5 0 0 1 4 20l6-11V4H9z"/></symbol>
  <symbol id="medkit" viewBox="0 0 24 24" fill="currentColor"><path fill-rule="evenodd" d="M2 6h20v15H2zm9 3v3H8v2h3v3h2v-3h3v-2h-3V9z"/><path d="M8 2h8v4h-2V4h-4v2H8z"/></symbol>
  <symbol id="sun" viewBox="0 0 24 24" fill="currentColor"><circle cx="12" cy="12" r="5"/><path d="M12 1v4M12 19v4M1 12h4M19 12h4M4.2 4.2 7 7M17 17l2.8 2.8M4.2 19.8 7 17M17 7l2.8-2.8" stroke="currentColor" stroke-width="2.5"/></symbol>
  <symbol id="play" viewBox="0 0 24 24" fill="currentColor"><path d="M6 3l15 9-15 9z"/></symbol>
  <symbol id="image" viewBox="0 0 24 24" fill="currentColor"><path fill-rule="evenodd" d="M2 4h20v16H2zm2 2v10l5-5 4 4 3-3 4 4V6z"/><circle cx="16" cy="9" r="2"/></symbol>
  <symbol id="pencil" viewBox="0 0 24 24" fill="currentColor"><path d="M3 21l1-5L15 5l4 4L8 20zM16.5 3.5 18 2l4 4-1.5 1.5z"/></symbol>
  <symbol id="thermometer" viewBox="0 0 24 24" fill="currentColor"><path d="M10 2h4v12a4.5 4.5 0 1 1-4 0z"/></symbol>
  <symbol id="bookmark" viewBox="0 0 24 24" fill="currentColor"><path d="M6 2h12v20l-6-5-6 5z"/></symbol>
  <symbol id="grid" viewBox="0 0 24 24" fill="currentColor"><path d="M3 3h8v8H3zm10 0h8v8h-8zM3 13h8v8H3zm10 0h8v8h-8z"/></symbol>
  <symbol id="list" viewBox="0 0 24 24" fill="currentColor"><path d="M3 4h3v3H3zm5 0h13v3H8zM3 10.5h3v3H3zm5 0h13v3H8zM3 17h3v3H3zm5 0h13v3H8z"/></symbol>
  <symbol id="link" viewBox="0 0 24 24"><path d="M10 14a5 5 0 0 0 7 0l3-3a5 5 0 0 0-7-7l-1 1M14 10a5 5 0 0 0-7 0l-3 3a5 5 0 0 0 7 7l1-1" fill="none" stroke="currentColor" stroke-width="2.5"/></symbol>
  <symbol id="refresh" viewBox="0 0 24 24" fill="currentColor"><path d="M20 12a8 8 0 1 1-2.3-5.7" fill="none" stroke="currentColor" stroke-width="2.5"/><path d="M21 3v7h-7z"/></symbol>
  <symbol id="mic" viewBox="0 0 24 24" fill="currentColor"><path d="M9 2h6v11a3 3 0 0 1-6 0z"/><path d="M5 11a7 7 0 0 0 14 0M12 18v4M8 22h8" fill="none" stroke="currentColor" stroke-width="2"/></symbol>
</svg>

<!-- Row 1 -->
<section class="slide c1 r1">
  <p class="kicker" style="top:16px">Infographic</p>
  <h2 class="heading" style="top:22px">Statistic Chart</h2>
  <div class="stat-lead tiny"><b>TECH – &nbsp;Title text here</b><br><br>A steady team builds growth by pairing sharp tools with open minds, shaping ideas that move with each client and each change in the market around them.</div>
  <p class="stat-note tiny">** Shared insight turns strong people into one clear team.</p>
  <div class="stat-row" style="top:44px">
    <div class="bar" style="left:18px;top:5px;width:140px"><em>90%</em></div>
    <div class="bar" style="left:18px;top:13px;width:110px"><em>70%</em></div>
    <div class="bar" style="left:18px;top:21px;width:94px"><em>60%</em></div>
    <div class="stat-badge"><span>2019</span></div>
    <div class="axis" style="top:32px"><span>10%</span><span>20%</span><span>30%</span><span>40%</span><span>50%</span><span>60%</span><span>70%</span><span>80%</span><span>90%</span><span>100%</span></div>
  </div>
  <div class="stat-row" style="top:102px">
    <div class="bar" style="left:18px;top:5px;width:140px"><em>90%</em></div>
    <div class="bar" style="left:18px;top:13px;width:110px"><em>70%</em></div>
    <div class="bar" style="left:18px;top:21px;width:126px"><em>80%</em></div>
    <div class="stat-badge"><span>2018</span></div>
    <div class="axis" style="top:32px"><span>10%</span><span>20%</span><span>30%</span><span>40%</span><span>50%</span><span>60%</span><span>70%</span><span>80%</span><span>90%</span><span>100%</span></div>
  </div>
  <div class="pager"></div>
  <div class="footer"><svg viewBox="0 0 284 9" preserveAspectRatio="none"><path d="M0 4 Q120 9 284 1 L284 9 L0 9Z" fill="var(--navy)"/></svg><span class="brand">Marrowind Labs</span></div>
</section>

<section class="slide c2 r1">
  <p class="kicker" style="top:16px">100% Infographic</p>
  <h2 class="heading" style="top:22px">Matrix Diagram</h2>
  <div class="matrix-axis"></div>
  <div class="matrix-base"></div>
  <span class="axis-label" style="left:34px;top:48px">High</span>
  <span class="axis-label" style="left:32px;top:128px">Low</span>
  <span class="axis-label" style="left:246px;top:126px">High</span>
  <span class="axis-label" style="left:122px;top:131px">Your text goes here</span>
  <div class="matrix">
    <div class="cell">Feature Text One</div>
    <div class="cell"><i></i>Feature Text Two</div>
    <div class="cell"><i></i>Feature Text Three</div>
    <div class="cell"><i></i>Feature Text Four</div>
    <div class="cell"><i></i>Feature Text Five</div>
    <div class="cell cell--on"><i></i>Feature Text Six</div>
    <div class="cell"><i></i>Feature Text Seven</div>
    <div class="cell"><i></i>Feature Text Eight</div>
    <div class="cell"><i></i>Feature Text Nine</div>
  </div>
  <p class="tiny" style="position:absolute;top:142px;width:100%;text-align:center;color:var(--grey)">** Shared insight turns strong people into one clear team, ready for each change.</p>
  <div class="pager"></div>
  <div class="footer"><svg viewBox="0 0 284 9" preserveAspectRatio="none"><path d="M0 4 Q120 9 284 1 L284 9 L0 9Z" fill="var(--navy)"/></svg><span class="brand">Marrowind Labs</span></div>
</section>

<section class="slide c3 r1">
  <h2 class="heading" style="top:18px;color:var(--ink)">Our Service</h2>
  <p class="svc-intro tiny">We help teams apply technology where it matters, joining business, tech and people into one shared direction so change becomes lasting value for every client we meet.</p>
  <div class="svc-band" role="img" aria-label="Photo of a modern open office space in blue tones"></div>
  <div class="svc-cols">
    <div class="svc"><svg><use href="#monitor"/></svg><b>Service One</b><p>Clear plans that link tools to real goals.</p></div>
    <div class="svc"><svg><use href="#list"/></svg><b>Service Two</b><p>Teams that learn and grow as one.</p></div>
    <div class="svc"><svg><use href="#search"/></svg><b>Service Three</b><p>Insight that guides each next step.</p></div>
    <div class="svc"><svg><use href="#monitor"/></svg><b>Service Four</b><p>Change that lasts beyond the project.</p></div>
  </div>
  <div class="pager"></div>
  <div class="footer"><svg viewBox="0 0 284 9" preserveAspectRatio="none"><path d="M0 4 Q120 9 284 1 L284 9 L0 9Z" fill="var(--navy)"/></svg><span class="brand">Marrowind Labs</span></div>
</section>

<section class="slide c4 r1">
  <div class="chart-photo" role="img" aria-label="Photo of an office interior in deep blue tones"></div>
  <svg class="chart-white" viewBox="0 0 284 164" preserveAspectRatio="none"><path d="M0 0 L0 164 L284 164 L284 150 Q150 140 70 60 Q40 20 0 0Z" fill="var(--white)"/></svg>
  <p class="chart-kick">100% Chart</p>
  <h2 class="chart-title">Chart<br>Diagram</h2>
  <div class="chart-card">
    <svg viewBox="0 0 174 70" style="position:absolute;left:0;top:0;width:174px;height:70px">
      <g stroke="var(--line)" stroke-width=".4">
        <line x1="12" y1="8" x2="168" y2="8"/><line x1="12" y1="18" x2="168" y2="18"/><line x1="12" y1="28" x2="168" y2="28"/>
        <line x1="12" y1="38" x2="168" y2="38"/><line x1="12" y1="48" x2="168" y2="48"/><line x1="12" y1="58" x2="168" y2="58"/>
      </g>
      <g fill="none" stroke-width=".8">
        <path d="M14 26 C40 10 50 60 70 60 S110 30 130 28 S150 10 165 8" stroke="#5b7ab8"/>
        <path d="M14 36 C40 36 50 8 70 10 S105 45 130 30 S150 40 165 30" stroke="#7d93c4"/>
        <path d="M14 14 C40 30 55 34 70 34 S110 30 130 36 S150 58 165 60" stroke="#3a5ea8"/>
      </g>
      <g fill="var(--white)" stroke="#3a5ea8" stroke-width=".6">
        <circle cx="14" cy="26" r="1.2"/><circle cx="70" cy="60" r="1.2"/><circle cx="130" cy="28" r="1.2"/><circle cx="165" cy="8" r="1.2"/>
        <circle cx="14" cy="36" r="1.2"/><circle cx="70" cy="10" r="1.2"/><circle cx="130" cy="30" r="1.2"/><circle cx="165" cy="30" r="1.2"/>
        <circle cx="14" cy="14" r="1.2"/><circle cx="70" cy="34" r="1.2"/><circle cx="130" cy="36" r="1.2"/><circle cx="165" cy="60" r="1.2"/>
      </g>
    </svg>
    <div class="donuts">
      <div class="donut"><svg viewBox="0 0 20 20"><circle cx="10" cy="10" r="7" fill="none" stroke="var(--pale)" stroke-width="3"/><circle cx="10" cy="10" r="7" fill="none" stroke="var(--navy)" stroke-width="3" stroke-dasharray="34 44" transform="rotate(-90 10 10)"/></svg>Text one</div>
      <div class="donut"><svg viewBox="0 0 20 20"><circle cx="10" cy="10" r="7" fill="none" stroke="var(--pale)" stroke-width="3"/><circle cx="10" cy="10" r="7" fill="none" stroke="var(--navy)" stroke-width="3" stroke-dasharray="20 44" transform="rotate(-90 10 10)"/></svg>Text two</div>
      <div class="donut"><svg viewBox="0 0 20 20"><circle cx="10" cy="10" r="7" fill="none" stroke="var(--pale)" stroke-width="3"/><circle cx="10" cy="10" r="7" fill="none" stroke="var(--navy)" stroke-width="3" stroke-dasharray="14 44" transform="rotate(-90 10 10)"/></svg>Text three</div>
    </div>
    <p class="chart-note tiny">Strong teams grow with every shared idea and each new step.</p>
  </div>
  <div class="pager"></div>
  <div class="footer"><svg viewBox="0 0 284 9" preserveAspectRatio="none"><path d="M0 4 Q120 9 284 1 L284 9 L0 9Z" fill="var(--navy)"/></svg><span class="brand">Marrowind Labs</span></div>
</section>

<!-- Row 2 -->
<section class="slide c1 r2">
  <h2 class="contact-title">GET IN<br><strong>CONTACT</strong><br>WITH US</h2>
  <p class="contact-lead tiny"><b>Let's talk change</b> – we pair people and technology to help your team move with clarity.</p>
  <ul class="contact-list">
    <li><svg><use href="#pin"/></svg>48 Harbour Lane, Sweden</li>
    <li><svg><use href="#phone"/></svg>+46 0000 1111 2222</li>
    <li><svg><use href="#mail"/></svg>hello@marrowindlabs.se</li>
    <li><svg><use href="#globe"/></svg>www.marrowindlabs.se</li>
  </ul>
  <div class="divider"></div>
  <div class="map" role="img" aria-label="Dark city street map with blue waterways and a location pin"></div>
  <div class="pager"></div>
  <div class="footer"><svg viewBox="0 0 284 9" preserveAspectRatio="none"><path d="M0 4 Q120 9 284 1 L284 9 L0 9Z" fill="var(--navy)"/></svg><span class="brand">Marrowind Labs</span></div>
</section>

<section class="slide slide--navy c2 r2">
  <div class="icons icons--dense">
    <svg><use href="#monitor"/></svg><svg><use href="#music"/></svg><svg><use href="#search"/></svg><svg><use href="#star"/></svg><svg><use href="#user"/></svg><svg><use href="#close"/></svg><svg><use href="#check"/></svg><svg><use href="#plus"/></svg><svg><use href="#gear"/></svg><svg><use href="#home"/></svg><svg><use href="#doc"/></svg><svg><use href="#clock"/></svg><svg><use href="#download"/></svg><svg><use href="#cloud"/></svg><svg><use href="#refresh"/></svg><svg><use href="#list"/></svg>
    <svg><use href="#lock"/></svg><svg><use href="#flag"/></svg><svg><use href="#bookmark"/></svg><svg><use href="#image"/></svg><svg><use href="#camera"/></svg><svg><use href="#pencil"/></svg><svg><use href="#pin"/></svg><svg><use href="#play"/></svg><svg><use href="#arrow"/></svg><svg><use href="#heart"/></svg><svg><use href="#mail"/></svg><svg><use href="#phone"/></svg><svg><use href="#chat"/></svg><svg><use href="#bell"/></svg><svg><use href="#cart"/></svg><svg><use href="#tag"/></svg>
    <svg><use href="#key"/></svg><svg><use href="#trash"/></svg><svg><use href="#folder"/></svg><svg><use href="#eye"/></svg><svg><use href="#globe"/></svg><svg><use href="#plane"/></svg><svg><use href="#mic"/></svg><svg><use href="#wifi"/></svg><svg><use href="#battery"/></svg><svg><use href="#sun"/></svg><svg><use href="#drop"/></svg><svg><use href="#link"/></svg><svg><use href="#grid"/></svg><svg><use href="#bars"/></svg><svg><use href="#pie"/></svg><svg><use href="#linechart"/></svg>
    <svg><use href="#calendar"/></svg><svg><use href="#briefcase"/></svg><svg><use href="#trophy"/></svg><svg><use href="#target"/></svg><svg><use href="#rocket"/></svg><svg><use href="#bulb"/></svg><svg><use href="#shield"/></svg><svg><use href="#cup"/></svg><svg><use href="#flask"/></svg><svg><use href="#medkit"/></svg><svg><use href="#thermometer"/></svg><svg><use href="#calculator"/></svg><svg><use href="#bank"/></svg><svg><use href="#star"/></svg><svg><use href="#user"/></svg><svg><use href="#home"/></svg>
    <svg><use href="#search"/></svg><svg><use href="#gear"/></svg><svg><use href="#doc"/></svg><svg><use href="#folder"/></svg><svg><use href="#lock"/></svg><svg><use href="#mail"/></svg><svg><use href="#cloud"/></svg><svg><use href="#camera"/></svg><svg><use href="#music"/></svg><svg><use href="#play"/></svg><svg><use href="#heart"/></svg><svg><use href="#check"/></svg><svg><use href="#close"/></svg><svg><use href="#plus"/></svg><svg><use href="#clock"/></svg><svg><use href="#bell"/></svg>
    <svg><use href="#chat"/></svg><svg><use href="#phone"/></svg><svg><use href="#pin"/></svg><svg><use href="#flag"/></svg><svg><use href="#tag"/></svg><svg><use href="#cart"/></svg><svg><use href="#key"/></svg><svg><use href="#image"/></svg><svg><use href="#pencil"/></svg><svg><use href="#trash"/></svg><svg><use href="#download"/></svg><svg><use href="#refresh"/></svg><svg><use href="#link"/></svg><svg><use href="#eye"/></svg><svg><use href="#wifi"/></svg><svg><use href="#mic"/></svg>
    <svg><use href="#bars"/></svg><svg><use href="#pie"/></svg><svg><use href="#linechart"/></svg><svg><use href="#grid"/></svg><svg><use href="#list"/></svg><svg><use href="#monitor"/></svg><svg><use href="#calendar"/></svg><svg><use href="#bookmark"/></svg><svg><use href="#globe"/></svg><svg><use href="#plane"/></svg><svg><use href="#sun"/></svg><svg><use href="#drop"/></svg><svg><use href="#battery"/></svg><svg><use href="#arrow"/></svg><svg><use href="#star"/></svg><svg><use href="#user"/></svg>
    <svg><use href="#search"/></svg><svg><use href="#arrow"/></svg><svg><use href="#play"/></svg><svg><use href="#image"/></svg>
  </div>
  <div class="pager"></div>
  <div class="footer"><svg viewBox="0 0 284 9" preserveAspectRatio="none"><path d="M0 4 Q120 9 284 1 L284 9 L0 9Z" fill="var(--white)"/></svg><span class="brand">Marrowind Labs</span></div>
</section>

<section class="slide c3 r2">
  <div class="icons icons--large">
    <svg><use href="#bank"/></svg><svg><use href="#calendar"/></svg><svg><use href="#briefcase"/></svg><svg><use href="#shield"/></svg><svg><use href="#linechart"/></svg><svg><use href="#calculator"/></svg><svg><use href="#tag"/></svg><svg><use href="#target"/></svg><svg><use href="#monitor"/></svg><svg><use href="#doc"/></svg><svg><use href="#rocket"/></svg><svg><use href="#globe"/></svg>
    <svg><use href="#bars"/></svg><svg><use href="#pie"/></svg><svg><use href="#trophy"/></svg><svg><use href="#cup"/></svg><svg><use href="#folder"/></svg><svg><use href="#briefcase"/></svg><svg><use href="#pencil"/></svg><svg><use href="#clock"/></svg><svg><use href="#refresh"/></svg><svg><use href="#gear"/></svg><svg><use href="#search"/></svg><svg><use href="#bulb"/></svg>
    <svg><use href="#target"/></svg><svg><use href="#refresh"/></svg><svg><use href="#bars"/></svg><svg><use href="#calculator"/></svg><svg><use href="#list"/></svg><svg><use href="#user"/></svg><svg><use href="#doc"/></svg><svg><use href="#grid"/></svg><svg><use href="#link"/></svg><svg><use href="#calculator"/></svg><svg><use href="#plane"/></svg><svg><use href="#key"/></svg>
    <svg><use href="#lock"/></svg><svg><use href="#tag"/></svg><svg><use href="#globe"/></svg><svg><use href="#shield"/></svg><svg><use href="#pie"/></svg><svg><use href="#clock"/></svg><svg><use href="#user"/></svg><svg><use href="#linechart"/></svg><svg><use href="#doc"/></svg><svg><use href="#home"/></svg><svg><use href="#calendar"/></svg><svg><use href="#chat"/></svg>
    <svg><use href="#lock"/></svg><svg><use href="#monitor"/></svg><svg><use href="#gear"/></svg><svg><use href="#bulb"/></svg><svg><use href="#bookmark"/></svg><svg><use href="#calculator"/></svg><svg><use href="#folder"/></svg><svg><use href="#home"/></svg><svg><use href="#mail"/></svg><svg><use href="#flag"/></svg><svg><use href="#target"/></svg><svg><use href="#star"/></svg>
  </div>
  <div class="pager"></div>
  <div class="footer"><svg viewBox="0 0 284 9" preserveAspectRatio="none"><path d="M0 4 Q120 9 284 1 L284 9 L0 9Z" fill="var(--navy)"/></svg><span class="brand">Marrowind Labs</span></div>
</section>

<section class="slide c4 r2">
  <div class="icons icons--large">
    <svg><use href="#battery"/></svg><svg><use href="#flask"/></svg><svg><use href="#cup"/></svg><svg><use href="#medkit"/></svg><svg><use href="#clock"/></svg><svg><use href="#pencil"/></svg><svg><use href="#pie"/></svg><svg><use href="#drop"/></svg><svg><use href="#flag"/></svg><svg><use href="#target"/></svg><svg><use href="#globe"/></svg><svg><use href="#grid"/></svg>
    <svg><use href="#link"/></svg><svg><use href="#heart"/></svg><svg><use href="#medkit"/></svg><svg><use href="#heart"/></svg><svg><use href="#drop"/></svg><svg><use href="#user"/></svg><svg><use href="#pencil"/></svg><svg><use href="#mail"/></svg><svg><use href="#close"/></svg><svg><use href="#key"/></svg><svg><use href="#bars"/></svg><svg><use href="#grid"/></svg>
    <svg><use href="#search"/></svg><svg><use href="#shield"/></svg><svg><use href="#user"/></svg><svg><use href="#play"/></svg><svg><use href="#drop"/></svg><svg><use href="#thermometer"/></svg><svg><use href="#trophy"/></svg><svg><use href="#user"/></svg><svg><use href="#star"/></svg><svg><use href="#clock"/></svg><svg><use href="#clock"/></svg><svg><use href="#target"/></svg>
    <svg><use href="#eye"/></svg><svg><use href="#user"/></svg><svg><use href="#sun"/></svg><svg><use href="#pencil"/></svg><svg><use href="#flask"/></svg><svg><use href="#cart"/></svg><svg><use href="#doc"/></svg><svg><use href="#pin"/></svg><svg><use href="#target"/></svg><svg><use href="#flag"/></svg><svg><use href="#play"/></svg><svg><use href="#trophy"/></svg>
    <svg><use href="#pin"/></svg><svg><use href="#pin"/></svg><svg><use href="#globe"/></svg><svg><use href="#medkit"/></svg><svg><use href="#flask"/></svg><svg><use href="#thermometer"/></svg><svg><use href="#search"/></svg><svg><use href="#trophy"/></svg><svg><use href="#flag"/></svg><svg><use href="#heart"/></svg><svg><use href="#bars"/></svg><svg><use href="#cup"/></svg>
  </div>
  <div class="pager"></div>
  <div class="footer"><svg viewBox="0 0 284 9" preserveAspectRatio="none"><path d="M0 4 Q120 9 284 1 L284 9 L0 9Z" fill="var(--navy)"/></svg><span class="brand">Marrowind Labs</span></div>
</section>

<!-- Row 3 -->
<section class="slide c1 r3">
  <div class="icons icons--ink">
    <svg><use href="#phone"/></svg><svg><use href="#mic"/></svg><svg><use href="#drop"/></svg><svg><use href="#pin"/></svg><svg><use href="#plane"/></svg><svg><use href="#arrow"/></svg><svg><use href="#pencil"/></svg><svg><use href="#link"/></svg><svg><use href="#refresh"/></svg><svg><use href="#arrow"/></svg><svg><use href="#user"/></svg><svg><use href="#link"/></svg><svg><use href="#cart"/></svg><svg><use href="#trash"/></svg>
    <svg><use href="#user"/></svg><svg><use href="#doc"/></svg><svg><use href="#download"/></svg><svg><use href="#home"/></svg><svg><use href="#pin"/></svg><svg><use href="#calendar"/></svg><svg><use href="#target"/></svg><svg><use href="#plane"/></svg><svg><use href="#close"/></svg><svg><use href="#shield"/></svg><svg><use href="#heart"/></svg><svg><use href="#bars"/></svg><svg><use href="#bell"/></svg><svg><use href="#lock"/></svg>
    <svg><use href="#star"/></svg><svg><use href="#search"/></svg><svg><use href="#chat"/></svg><svg><use href="#bulb"/></svg><svg><use href="#clock"/></svg><svg><use href="#eye"/></svg><svg><use href="#home"/></svg><svg><use href="#plus"/></svg><svg><use href="#search"/></svg><svg><use href="#pencil"/></svg><svg><use href="#cloud"/></svg><svg><use href="#close"/></svg><svg><use href="#plus"/></svg><svg><use href="#trash"/></svg>
    <svg><use href="#flag"/></svg><svg><use href="#key"/></svg><svg><use href="#trophy"/></svg><svg><use href="#pin"/></svg><svg><use href="#camera"/></svg><svg><use href="#sun"/></svg><svg><use href="#cloud"/></svg><svg><use href="#music"/></svg><svg><use href="#play"/></svg><svg><use href="#image"/></svg><svg><use href="#grid"/></svg><svg><use href="#refresh"/></svg><svg><use href="#link"/></svg><svg><use href="#folder"/></svg>
    <svg><use href="#doc"/></svg><svg><use href="#plane"/></svg><svg><use href="#target"/></svg><svg><use href="#clock"/></svg><svg><use href="#gear"/></svg><svg><use href="#battery"/></svg><svg><use href="#drop"/></svg><svg><use href="#briefcase"/></svg><svg><use href="#list"/></svg><svg><use href="#cup"/></svg><svg><use href="#folder"/></svg><svg><use href="#monitor"/></svg><svg><use href="#mail"/></svg><svg><use href="#globe"/></svg>
    <svg><use href="#linechart"/></svg><svg><use href="#gear"/></svg><svg><use href="#pencil"/></svg><svg><use href="#bookmark"/></svg><svg><use href="#flask"/></svg><svg><use href="#trash"/></svg><svg><use href="#pencil"/></svg><svg><use href="#briefcase"/></svg><svg><use href="#globe"/></svg><svg><use href="#wifi"/></svg><svg><use href="#thermometer"/></svg><svg><use href="#shield"/></svg><svg><use href="#pin"/></svg><svg><use href="#linechart"/></svg>
    <svg><use href="#monitor"/></svg><svg><use href="#grid"/></svg><svg><use href="#battery"/></svg><svg><use href="#battery"/></svg><svg><use href="#sun"/></svg><svg><use href="#gear"/></svg><svg><use href="#link"/></svg><svg><use href="#monitor"/></svg><svg><use href="#bulb"/></svg><svg><use href="#list"/></svg><svg><use href="#pie"/></svg><svg><use href="#check"/></svg><svg><use href="#arrow"/></svg><svg><use href="#bars"/></svg>
  </div>
  <div class="pager"></div>
  <div class="footer"><svg viewBox="0 0 284 9" preserveAspectRatio="none"><path d="M0 4 Q120 9 284 1 L284 9 L0 9Z" fill="var(--navy)"/></svg><span class="brand">Marrowind Labs</span></div>
</section>

<section class="slide slide--sky c2 r3">
  <div class="icons icons--sky">
    <svg><use href="#monitor"/></svg><svg><use href="#monitor"/></svg><svg><use href="#doc"/></svg><svg><use href="#grid"/></svg><svg><use href="#calendar"/></svg><svg><use href="#check"/></svg><svg><use href="#doc"/></svg><svg><use href="#list"/></svg><svg><use href="#camera"/></svg><svg><use href="#folder"/></svg><svg><use href="#doc"/></svg><svg><use href="#monitor"/></svg><svg><use href="#image"/></svg><svg><use href="#monitor"/></svg><svg><use href="#refresh"/></svg><svg><use href="#linechart"/></svg>
    <svg><use href="#play"/></svg><svg><use href="#mic"/></svg><svg><use href="#play"/></svg><svg><use href="#music"/></svg><svg><use href="#mic"/></svg><svg><use href="#wifi"/></svg><svg><use href="#eye"/></svg><svg><use href="#eye"/></svg><svg><use href="#wifi"/></svg><svg><use href="#wifi"/></svg><svg><use href="#star"/></svg><svg><use href="#globe"/></svg><svg><use href="#play"/></svg><svg><use href="#grid"/></svg><svg><use href="#heart"/></svg><svg><use href="#bookmark"/></svg>
    <svg><use href="#chat"/></svg><svg><use href="#chat"/></svg><svg><use href="#chat"/></svg><svg><use href="#chat"/></svg><svg><use href="#cloud"/></svg><svg><use href="#list"/></svg><svg><use href="#doc"/></svg><svg><use href="#star"/></svg><svg><use href="#trash"/></svg><svg><use href="#link"/></svg><svg><use href="#music"/></svg><svg><use href="#camera"/></svg><svg><use href="#key"/></svg><svg><use href="#bell"/></svg><svg><use href="#tag"/></svg><svg><use href="#user"/></svg>
    <svg><use href="#cart"/></svg><svg><use href="#cart"/></svg><svg><use href="#close"/></svg><svg><use href="#cart"/></svg><svg><use href="#briefcase"/></svg><svg><use href="#cart"/></svg><svg><use href="#briefcase"/></svg><svg><use href="#cart"/></svg><svg><use href="#tag"/></svg><svg><use href="#tag"/></svg><svg><use href="#shield"/></svg><svg><use href="#user"/></svg><svg><use href="#plus"/></svg><svg><use href="#play"/></svg><svg><use href="#globe"/></svg><svg><use href="#star"/></svg>
    <svg><use href="#grid"/></svg><svg><use href="#briefcase"/></svg><svg><use href="#list"/></svg><svg><use href="#lock"/></svg><svg><use href="#cart"/></svg><svg><use href="#folder"/></svg><svg><use href="#lock"/></svg><svg><use href="#lock"/></svg><svg><use href="#download"/></svg><svg><use href="#refresh"/></svg><svg><use href="#star"/></svg><svg><use href="#phone"/></svg><svg><use href="#chat"/></svg><svg><use href="#doc"/></svg><svg><use href="#user"/></svg><svg><use href="#link"/></svg>
    <svg><use href="#grid"/></svg><svg><use href="#plus"/></svg><svg><use href="#plus"/></svg><svg><use href="#check"/></svg><svg><use href="#target"/></svg><svg><use href="#image"/></svg><svg><use href="#grid"/></svg><svg><use href="#image"/></svg><svg><use href="#image"/></svg><svg><use href="#pencil"/></svg><svg><use href="#pencil"/></svg><svg><use href="#pencil"/></svg><svg><use href="#doc"/></svg><svg><use href="#plus"/></svg><svg><use href="#close"/></svg><svg><use href="#lock"/></svg>
    <svg><use href="#arrow"/></svg><svg><use href="#refresh"/></svg><svg><use href="#arrow"/></svg><svg><use href="#arrow"/></svg><svg><use href="#close"/></svg><svg><use href="#arrow"/></svg><svg><use href="#refresh"/></svg><svg><use href="#refresh"/></svg><svg><use href="#download"/></svg><svg><use href="#star"/></svg><svg><use href="#sun"/></svg><svg><use href="#wifi"/></svg><svg><use href="#tag"/></svg><svg><use href="#search"/></svg><svg><use href="#plus"/></svg><svg><use href="#close"/></svg>
    <svg><use href="#target"/></svg><svg><use href="#gear"/></svg><svg><use href="#arrow"/></svg><svg><use href="#arrow"/></svg><svg><use href="#arrow"/></svg><svg><use href="#doc"/></svg><svg><use href="#image"/></svg><svg><use href="#pencil"/></svg><svg><use href="#monitor"/></svg><svg><use href="#search"/></svg><svg><use href="#user"/></svg><svg><use href="#camera"/></svg><svg><use href="#check"/></svg><svg><use href="#grid"/></svg><svg><use href="#refresh"/></svg><svg><use href="#link"/></svg>
    <svg><use href="#clock"/></svg><svg><use href="#sun"/></svg><svg><use href="#cloud"/></svg><svg><use href="#drop"/></svg><svg><use href="#pin"/></svg>
  </div>
  <div class="pager"></div>
  <div class="footer"><svg viewBox="0 0 284 9" preserveAspectRatio="none"><path d="M0 4 Q120 9 284 1 L284 9 L0 9Z" fill="var(--white)"/></svg><span class="brand">Marrowind Labs</span></div>
</section>

<div class="features">
  <p>Smart Layered - Vector - Editable Charts - Excel Tables -</p>
  <p>Infograph Elements - Fully Editable - Animated &amp; Non-Animated Version</p>
</div>

</body>
</html>
```